Startup online payment business - Sporting / Golf, Swift Tee payment

Background:
Our business name is "Swift Tee" we provide online payments for golfing services via our website. We currently have a logo used on our website. No other design style has been developed. Our aim is to remove cash payments for service at golf clubs.

Our Key Values:
Quick and easy
Formal and polite
Fun with professional boundary
Mate-ship relationships
100% online digital

What we want from you:
Marketing design to be used on posters and stickers in a retail setting to direct customers to our online payment Chanel.
Design must incorporate attached logo, URL swifttee.com.au and our key values can act as a guide the type of design. We have used color Hex#007672 for logo background. We are open to use other colors.

Target Market(s)

Golf clubs and golf players

Industry/Entity Type

Golf Course

Font styles to use
Sans Serif

Requirements
Must have
• Directions to online payment via URL: swifttee.com.au
Nice to have
• We like the idea of the slogan: No Cash - No worries. Have attached home screen that will be available from URL link. Consideration if using mobile phone in image. Push the online payment and steps 1. Visit swifttee.com 2. Select club 3. Confirm payment
Should not have
• Cartoons

```html
<!DOCTYPE html>
<html lang="en">
<head>
<meta charset="utf-8">
<title>Swift Tee – No Cash, No Worries</title>
<link rel="stylesheet" href="https://fonts.googleapis.com/css2?family=Arimo:wght@400;700&family=Tinos:wght@400;700&display=swap">
<style>
  :root {
    --teal: #079490;
    --teal-logo: #007672;
    --teal-deep: #023e3e;
    --teal-dark: #021f1f;
    --sky: #3bb4c6;
    --white: #ffffff;
    --ink: #231f20;
    --rule-top: #0a8580;
    --rule-bottom: #013331;
  }
  html, body {
    margin: 0;
    padding: 0;
    width: 1200px;
    height: 938px;
    overflow: hidden;
    background: var(--white);
  }
  .canvas {
    position: relative;
    width: 1200px;
    height: 938px;
    overflow: hidden;
    font-family: "Tinos", "Times New Roman", serif;
  }

  /* Print size markers */
  .dimension { position: absolute; }
  .dimension-svg { position: absolute; left: 0; top: 0; }
  .dimension-label {
    position: absolute;
    font-family: "Arimo", Arial, sans-serif;
    font-size: 38px;
    color: var(--ink);
    line-height: 1;
  }
  .dimension-label--height {
    left: 8px;
    top: 420px;
    transform: rotate(-90deg);
  }
  .dimension-label--width {
    left: 612px;
    top: 890px;
  }

  /* Poster */
  .poster {
    position: absolute;
    left: 72px;
    top: 0;
    width: 1128px;
    height: 861px;
    overflow: hidden;
  }
  .poster-backdrop { position: absolute; left: 0; top: 0; }

  .header-band {
    position: absolute;
    left: 0;
    top: 0;
    width: 1128px;
    height: 211px;
    background: linear-gradient(to bottom, var(--teal) 0%, #05716e 45%, var(--teal-deep) 100%);
  }

  .brand-box {
    position: absolute;
    left: 49px;
    top: 27px;
    width: 223px;
    height: 184px;
    background: var(--white);
  }
  .brand-box-inner {
    position: absolute;
    left: 11px;
    top: 13px;
    width: 202px;
    height: 160px;
    background: var(--teal-logo);
    display: flex;
    align-items: center;
    justify-content: center;
  }
  .brand-name {
    font-family: "Arimo", Arial, sans-serif;
    font-weight: 700;
    font-size: 32px;
    color: var(--white);
    letter-spacing: 1px;
  }

  .headline {
    position: absolute;
    left: 330px;
    top: 32px;
    width: 765px;
    margin: 0;
    text-align: center;
    font-family: "Tinos", "Times New Roman", serif;
    font-weight: 700;
    font-size: 77px;
    line-height: 1;
    color: var(--white);
    white-space: nowrap;
  }

  .rule {
    position: absolute;
    background: linear-gradient(to bottom, var(--rule-top), var(--rule-bottom));
  }
  .rule--header { left: 336px; top: 117px; width: 753px; height: 11px; }

  .site-url {
    position: absolute;
    margin: 0;
    font-family: "Arimo", Arial, sans-serif;
    font-weight: 700;
    line-height: 1;
    color: var(--white);
    white-space: nowrap;
  }
  .site-url--header {
    left: 330px;
    top: 121px;
    width: 765px;
    text-align: center;
    font-size: 71px;
  }
  .site-url--footer {
    left: 38px;
    top: 786px;
    font-size: 55px;
  }

  .intro {
    position: absolute;
    left: 64px;
    width: 1040px;
    margin: 0;
    font-size: 35px;
    line-height: 38.5px;
    color: var(--ink);
  }
  .intro--mission { top: 224px; }
  .intro--cashless { top: 312px; }

  .value {
    position: absolute;
    margin: 0;
    font-size: 52px;
    line-height: 1;
    color: var(--ink);
    white-space: nowrap;
  }
  .value::before {
    content: "";
    position: absolute;
    left: -27px;
    top: 15px;
    width: 12px;
    height: 22px;
    background: var(--ink);
    clip-path: polygon(0 0, 100% 50%, 0 100%);
  }
  .value--quick { left: 273px; top: 442px; }
  .value--formal { left: 648px; top: 442px; }
  .value--fun { left: 324px; top: 520px; }
  .value--mateship { left: 408px; top: 602px; }
  .value--digital { left: 447px; top: 679px; }

  .rule--value-1 { left: 258px; top: 503px; width: 712px; height: 10px; }
  .rule--value-2 { left: 264px; top: 581px; width: 712px; height: 10px; }
  .rule--value-3 { left: 377px; top: 664px; width: 485px; height: 9px; }
  .rule--value-4 { left: 412px; top: 740px; width: 416px; height: 9px; }
</style>
</head>
<body>
<div class="canvas">

  <svg class="dimension-svg" width="1200" height="938" viewBox="0 0 1200 938" aria-hidden="true">
    <g stroke="#231f20" stroke-width="1.5" fill="#231f20">
      <line x1="27" y1="6" x2="27" y2="358"/>
      <line x1="27" y1="519" x2="27" y2="870"/>
      <polygon points="27,0 22,11 32,11" stroke="none"/>
      <polygon points="27,877 22,866 32,866" stroke="none"/>
      <line x1="80" y1="910" x2="552" y2="910"/>
      <line x1="713" y1="910" x2="1193" y2="910"/>
      <polygon points="73,910 84,905 84,915" stroke="none"/>
      <polygon points="1200,910 1189,905 1189,915" stroke="none"/>
    </g>
  </svg>
  <span class="dimension-label dimension-label--height">7”</span>
  <span class="dimension-label dimension-label--width">9”</span>

  <main class="poster">
    <svg class="poster-backdrop" width="1128" height="861" viewBox="72 0 1128 861" aria-hidden="true">
      <defs>
        <linearGradient id="baseTeal" x1="0" y1="0" x2="1" y2="0.35">
          <stop offset="0" stop-color="#079490"/>
          <stop offset="0.4" stop-color="#058a86"/>
          <stop offset="0.62" stop-color="#034846"/>
          <stop offset="0.75" stop-color="#021f1f"/>
          <stop offset="1" stop-color="#021f1f"/>
        </linearGradient>
        <linearGradient id="whiteSheet" x1="0" y1="0" x2="0.3" y2="1">
          <stop offset="0" stop-color="#ffffff"/>
          <stop offset="0.75" stop-color="#ffffff"/>
          <stop offset="1" stop-color="#e4e4e4"/>
        </linearGradient>
      </defs>
      <rect x="72" y="0" width="1128" height="861" fill="url(#baseTeal)"/>
      <path d="M1200,211 C1195,560 1060,780 877,849 L1082,861 L1200,861 Z" fill="#3bb4c6"/>
      <path d="M72,211 L1200,211 C1195,560 1060,780 877,849 C450,760 100,560 72,214 Z" fill="url(#whiteSheet)"/>
    </svg>

    <header class="header-band">
      <div class="brand-box">
        <div class="brand-box-inner">
          <span class="brand-name">Swift Tee</span>
        </div>
      </div>
      <h1 class="headline">No Cash - No Worries</h1>
      <div class="rule rule--header"></div>
      <p class="site-url site-url--header">swifttee.com.au</p>
    </header>

    <p class="intro intro--mission">Swift Tee is here to support Golf Clubs embrace new stategies&nbsp; for success in a rapidly changing world.</p>
    <p class="intro intro--cashless">Moving toward a future cashless society, Swift Tee are developing new mobile payment methods in order for Clubs to cater for the next generation of players and community expectations.</p>

    <p class="value value--quick">Quick and easy</p>
    <p class="value value--formal">Formal and polite</p>
    <div class="rule rule--value-1"></div>

    <p class="value value--fun">Fun with professional boundary</p>
    <div class="rule rule--value-2"></div>

    <p class="value value--mateship">Mate-ship relationships</p>
    <div class="rule rule--value-3"></div>

    <p class="value value--digital">100% online digital</p>
    <div class="rule rule--value-4"></div>

    <p class="site-url site-url--footer">swifttee.com.au</p>
  </main>
</div>
</body>
</html>
```